Quiet Harbour Counselling Flyer Design

I am a counsellor about to set up in independant practice. I need my flyer to tie in with my business card design. It should be simple / elegant on the outside face- dark blue background with white text. . The internal face could have a splash of colour to make it interesting. Perhaps an image of 'waves with the text over the top. With the quote underneath 'you can't stop the waves, but you can learn to surf'. Perhaps a border separating text info from quote. I want the text to be varying sizes and fonts so that it looks more interesting but still should feel simple. I have included the text I need, in the page order however I am open to suggestions about how this will look graphically. Please see business card design.i would like 'stars can't shine without darkness' to match business card.

I need it to look professional, elegant, simplistic but eye catching.

The logo was designed by inkmerrow

```html
<!DOCTYPE html>
<html lang="en">
<head>
<meta charset="utf-8">
<title>Quiet Harbour Counselling – Flyer</title>
<link href="https://fonts.googleapis.com/css2?family=Jost:ital,wght@0,400;1,300&family=Pinyon+Script&display=swap" rel="stylesheet">
<style>
  :root {
    --backdrop: #a19e9e;
    --navy-top: #24489a;
    --navy-mid: #173584;
    --navy-deep: #0a1248;
    --wave-tone: #0e2266;
    --white: #ffffff;
    --cream: #f5ecd9;
  }
  * { margin: 0; padding: 0; box-sizing: border-box; }
  html, body { width: 1200px; height: 1000px; overflow: hidden; background: var(--backdrop); }
  .canvas { position: relative; width: 1200px; height: 1000px; }
  .flyer {
    position: absolute; left: 71px; top: 132px; width: 1059px; height: 756px;
    overflow: hidden; color: var(--white);
    font-family: "Jost", sans-serif;
    background: linear-gradient(180deg, var(--navy-top) 0%, var(--navy-mid) 45%, var(--navy-deep) 100%);
    box-shadow: 4px 4px 6px rgba(0,0,0,.35);
  }
  .panel-fold {
    position: absolute; top: 0; width: 30px; height: 100%;
    background: linear-gradient(90deg, rgba(0,0,0,0), rgba(0,0,0,.14), rgba(0,0,0,0));
  }
  .panel-fold--first { left: 330px; }
  .panel-fold--second { left: 708px; }
  .wave-artwork {
    position: absolute; left: 0; top: 380px; width: 1059px; height: 150px;
    background: linear-gradient(180deg, rgba(14,34,102,0) 0%, rgba(14,34,102,.55) 50%, rgba(14,34,102,0) 100%);
  }
  .heading { position: absolute; top: 40px; font-size: 38px; font-weight: 400; letter-spacing: .3px; line-height: 52px; }
  .heading--left { left: 47px; }
  .heading--right { right: 45px; }
  .intro { position: absolute; left: 44px; top: 124px; width: 276px; font-size: 14px; line-height: 28px; }
  .contact-list { position: absolute; left: 40px; top: 222px; list-style: none; }
  .contact-item { display: flex; align-items: center; height: 34px; margin-bottom: 7px; font-size: 13.5px; }
  .contact-item svg { width: 34px; height: 34px; margin-right: 24px; flex: none; }
  .contact-item--phone { font-size: 16px; }
  .script { font-family: "Pinyon Script", cursive; color: var(--white); position: absolute; white-space: nowrap; }
  .tagline-centre { left: 368px; top: 286px; font-size: 28px; }
  .tagline-left-1 { left: 20px; top: 617px; font-size: 27px; }
  .tagline-left-2 { left: 173px; top: 665px; font-size: 27px; }
  .feelings { position: absolute; right: 47px; top: 116px; list-style: none; text-align: right; font-size: 15px; line-height: 27.7px; }
  .stat { position: absolute; left: 747px; top: 391px; font-size: 11px; font-style: italic; font-weight: 300; line-height: 15px; }
  .stat p + p { margin-top: 14px; }
  .stat .indent-1 { padding-left: 105px; display: block; }
  .stat .indent-2 { padding-left: 143px; display: block; }
  .brand-name {
    position: absolute; right: 30px; top: 612px; text-align: right;
    font-family: "Jost", sans-serif; font-weight: 400; font-size: 30px; line-height: 34px; color: var(--cream);
  }
</style>
</head>
<body>
<div class="canvas">
  <section class="flyer">
    <div class="panel-fold panel-fold--first"></div>
    <div class="panel-fold panel-fold--second"></div>
    <div class="wave-artwork" role="img" aria-label="Flowing dark blue wave swooshes with faint stars across the flyer"></div>

    <h2 class="heading heading--left">Get in touch</h2>
    <p class="intro">If you are curious about how Quiet Harbour could help you simply send me an email or give me a call.</p>
    <ul class="contact-list">
      <li class="contact-item contact-item--phone">
        <svg viewBox="0 0 34 34" aria-hidden="true"><rect x="1" y="1" width="32" height="32" rx="7" fill="#0d1c5e" stroke="#fff" stroke-width="1.5"/><path d="M11 8c-2 1-3 3-2 6 2 6 6 10 11 12 2 1 4 0 5-2l-3-3-3 2c-3-1-5-4-6-6l2-3z" fill="#fff"/></svg>
        07700900481
      </li>
      <li class="contact-item">
        <svg viewBox="0 0 34 34" aria-hidden="true"><rect x="1" y="1" width="32" height="32" rx="7" fill="#0d1c5e" stroke="#fff" stroke-width="1.5"/><rect x="7" y="11" width="20" height="13" fill="#fff"/><path d="M7 11l10 8 10-8" fill="none" stroke="#0d1c5e" stroke-width="1.3"/></svg>
        www.quietharbourcounselling.co.uk
      </li>
      <li class="contact-item">
        <svg viewBox="0 0 34 34" aria-hidden="true"><rect x="1" y="1" width="32" height="32" rx="7" fill="#0d1c5e" stroke="#fff" stroke-width="1.5"/><circle cx="17" cy="17" r="10" fill="#fff"/><text x="17" y="19.5" text-anchor="middle" font-size="7" font-family="Jost, sans-serif" fill="#0d1c5e">www</text></svg>
        quietharbour121@harbourmail.co.uk
      </li>
    </ul>
    <p class="script tagline-left-1">By changing nothing,</p>
    <p class="script tagline-left-2">nothing changes</p>

    <p class="script tagline-centre">Stars can’t shine without darkness</p>

    <h2 class="heading heading--right">Sound familiar?</h2>
    <ul class="feelings">
      <li>I’m struggling…</li>
      <li>I’m feeling stressed…</li>
      <li>Life is overwhelming me…</li>
      <li>I keep repeating the same mistakes…</li>
      <li>I’m unhappy…</li>
      <li>I feel so alone…</li>
      <li>I need someone to turn to…</li>
      <li>I want things to change…</li>
    </ul>
    <div class="stat">
      <p>4 out of 5 of us will feel anxious, stressed,<br>depressed and stuck at some point in life.</p>
      <p>If this sound likes you<span class="indent-1">Quiet Harbour</span><span class="indent-2">Counselling could help.</span></p>
    </div>
    <p class="brand-name">Quiet Harbour<br>Counselling</p>
  </section>
</div>
</body>
</html>
```